Investigation Before Elimination

Create a very professional and eye-catching Infographic for Birchline Supply that is intended to convey to retailers that they should investigate why products are NOT selling in the Birchline Supply store before they apply a discount to get rid of it. The infographic should capture all of the questions they should think about before making cutting the price. See the attachment for details on wording.

Target Market(s)

Birchline Supply Business Owners

Industry/Entity Type

Retail

Font styles to use
Sans Serif

Requirements
Must have
• Any product in the infographic must be home improvement related product. See our website for ideas:
https://www.birchlinesupply.example/?utm_source=google&utm_medium=cpc&gclid=QwpLMnRt8X4ZkHFpTvB3YcNE7q_rs2JkWbhv8mYd204_7Gf-xlPQe4pm88sRyTzGk2Vq6-Lbh-yXpLW-mdNwBnq_CvA&gclsrc=aw.ds

* Must be in Birchline Supply related colors
* Must be fun, exciting, eye-catching, unique, and clever
* 1-Page preferable but no more than two standard 8-1/2"x11"
* See the attachment for details on wording.
Should not have
• N/A

```html
<!DOCTYPE html>
<html lang="en">
<head>
<meta charset="utf-8">
<title>Investigation Before Elimination – Birchline Supply</title>
<link rel="stylesheet" href="https://fonts.googleapis.com/css2?family=Roboto:wght@400;500;700&family=Roboto+Slab:wght@700;800&display=swap">
<style>
:root{
  --ink:#3f3f3f;
  --body:#4a4a4a;
  --brand:#e31837;
  --c1:#b01e23;
  --c2:#e31837;
  --c3:#f0822b;
  --c4:#f2e63a;
  --c5:#7dc242;
  --c6:#6ab7e6;
  --c7:#8e6aa3;
  --c8:#e8237a;
  --hub:#404040;
  --band:#e6e6e6;
  --footer:#8c8787;
}
*{margin:0;padding:0;box-sizing:border-box}
html,body{width:1200px;height:927px;overflow:hidden;background:#fff}
body{font-family:"Roboto",Arial,sans-serif;color:var(--body)}
.canvas{position:relative;width:1200px;height:927px;overflow:hidden;background:#fff}

.title{position:absolute;left:53px;top:68px;font-family:"Roboto Slab",Georgia,serif;font-weight:800;font-size:64px;line-height:1;letter-spacing:-1px;color:var(--ink);white-space:nowrap}
.title .before{display:inline-block;background:var(--ink);color:#fff;font-family:"Roboto",Arial,sans-serif;font-weight:700;font-size:30px;letter-spacing:1px;padding:4px 12px;vertical-align:12px;margin:0 14px 0 10px}
.title .accent{color:var(--brand)}
.rule{position:absolute;left:53px;top:148px;width:876px;height:1px;background:#bdbdbd}
.brand{position:absolute;left:972px;top:92px;display:flex;align-items:center;gap:10px;font-family:"Roboto Slab",Georgia,serif;font-weight:800;font-size:27px;color:var(--brand);white-space:nowrap}
.brand .mark{width:22px;height:22px;background:var(--brand)}

.lead{position:absolute;left:60px;width:1080px;top:180px;text-align:center;font-weight:700;font-size:19.5px;line-height:26px;color:var(--body)}
.sublead{position:absolute;left:60px;width:1080px;top:263px;text-align:center;font-size:16.5px;line-height:24px;color:var(--body)}

.wheel{position:absolute;left:0;top:0;width:1200px;height:927px}
.hub-text{position:absolute;left:470px;top:626px;width:258px;text-align:center;color:#fff;font-size:17px;line-height:22px}
.hub-text .yes{display:inline-block;background:var(--brand);font-weight:700;padding:0 5px;line-height:20px}

.num{position:absolute;font-family:"Roboto",Arial,sans-serif;font-weight:700;font-size:40px;line-height:1}
.step{position:absolute;font-size:12.5px;line-height:15px;color:var(--body)}
.step h3{font-size:14px;line-height:17px;font-weight:700;margin-bottom:5px}
.step.right{text-align:right}

.s1 h3,.n1{color:var(--c1)}
.s2 h3,.n2{color:var(--c2)}
.s3 h3,.n3{color:var(--c3)}
.s4 h3{color:var(--ink)}
.n4{color:var(--c4)}
.s5 h3,.n5{color:var(--c5)}
.s6 h3,.n6{color:var(--c6)}
.s7 h3,.n7{color:var(--c7)}
.s8 h3,.n8{color:var(--c8)}

.resources{position:absolute;left:0;top:733px;width:1200px;height:119px;background:var(--band);text-align:center}
.resources p{margin-top:26px;font-size:20px;color:#333}
.links{display:flex;justify-content:center;align-items:center;margin-top:14px;font-size:16.5px;color:var(--brand)}
.links a{color:var(--brand);text-decoration:none;padding:0 26px}
.links a sup{font-size:9px;font-style:italic;font-weight:700}
.links .sep{width:1px;height:26px;background:#9a9a9a}

.footer{position:absolute;left:0;top:852px;width:1200px;height:75px;background:var(--footer);color:#fff;font-size:15px;display:flex;align-items:center;justify-content:center;gap:8px}
.footer svg{vertical-align:middle}
.footer .gap{width:10px}
.stripe-dark{position:absolute;left:0;top:852px;width:51px;height:75px;background:var(--ink)}
.stripe-red{position:absolute;left:51px;top:852px;width:23px;height:75px;background:var(--brand)}
</style>
</head>
<body>
<main class="canvas">
  <h1 class="title">Investigation<span class="before">BEFORE</span><span class="accent">Elimination</span></h1>
  <div class="rule"></div>
  <div class="brand"><span class="mark"></span>Birchline Supply</div>

  <p class="lead">Dead stock in your store rapidly eats away at profits, drives up the cost of doing business, and occupies valuable shelf space that would be better served by fresh and more productive products. To address this issue, a typical knee-jerk response is marking down the product and attempting to sell it at a discount.</p>
  <p class="sublead">Though this is a better approach than simply hoping it sells ‘one day’, applying a markdown should be used only as a last resort after sales floor investigation takes place for common execution issues that are known to hamper sales;</p>

  <svg class="wheel" viewBox="0 0 1200 927" aria-hidden="true">
    <g transform="translate(599 727)">
      <path fill="var(--c1)" d="M-244 0A244 244 0 0 1-225.4-93.4L-147.8-61.2A160 160 0 0 0-160 0Z"/>
      <path fill="var(--c2)" d="M-225.4-93.4A244 244 0 0 1-172.5-172.5L-113.1-113.1A160 160 0 0 0-147.8-61.2Z"/>
      <path fill="var(--c3)" d="M-172.5-172.5A244 244 0 0 1-93.4-225.4L-61.2-147.8A160 160 0 0 0-113.1-113.1Z"/>
      <path fill="var(--c4)" d="M-93.4-225.4A244 244 0 0 1 0-244L0-160A160 160 0 0 0-61.2-147.8Z"/>
      <path fill="var(--c5)" d="M0-244A244 244 0 0 1 93.4-225.4L61.2-147.8A160 160 0 0 0 0-160Z"/>
      <path fill="var(--c6)" d="M93.4-225.4A244 244 0 0 1 172.5-172.5L113.1-113.1A160 160 0 0 0 61.2-147.8Z"/>
      <path fill="var(--c7)" d="M172.5-172.5A244 244 0 0 1 225.4-93.4L147.8-61.2A160 160 0 0 0 113.1-113.1Z"/>
      <path fill="var(--c8)" d="M225.4-93.4A244 244 0 0 1 244 0L160 0A160 160 0 0 0 147.8-61.2Z"/>
      <path fill="#fff" opacity=".68" d="M-182 0A182 182 0 0 1 182 0L160 0A160 160 0 0 0-160 0Z"/>
      <path fill="var(--hub)" d="M-160 0A160 160 0 0 1 160 0Z"/>
    </g>
    <g fill="none" stroke-width="1.6" stroke-dasharray="2 3">
      <polyline stroke="var(--c1)" points="332,657 361,672"/>
      <polyline stroke="var(--c2)" points="375,559 403,570"/>
      <polyline stroke="var(--c3)" points="403,451 432,457 458,495"/>
      <polyline stroke="var(--c4)" points="516,362 551,362 551,480"/>
      <polyline stroke="var(--c5)" points="700,362 648,362 648,480"/>
      <polyline stroke="var(--c6)" points="790,451 763,457 738,492"/>
      <polyline stroke="var(--c7)" points="820,561 795,570"/>
      <polyline stroke="var(--c8)" points="863,653 835,672"/>
    </g>
  </svg>

  <p class="hub-text">It is only after saying <span class="yes">“YES”</span> to these questions should an item be considered for a markdown strategy</p>

  <span class="num n1" style="left:290px;top:640px">01</span>
  <div class="step s1" style="left:91px;top:638px;width:195px">
    <h3>Is the product physically there?</h3>
    <p>One of the most typical issues is that the item is no longer existent (i.e. ghost inventory).</p>
  </div>

  <span class="num n2" style="left:328px;top:543px">02</span>
  <div class="step s2" style="left:91px;top:545px;width:235px">
    <h3>Is the item merchandised properly - Is it in plain view of the customer?</h3>
    <p>Find out if it is stuck in the backroom, top stock, or buried behind other products.</p>
  </div>

  <span class="num n3" style="left:357px;top:433px">03</span>
  <div class="step s3" style="left:91px;top:435px;width:258px">
    <h3>Is the item priced competitively?</h3>
    <p>In today’s price sensitive market, making sure the cost of the SKU is in line with the customer expectation is key.</p>
  </div>

  <span class="num n4" style="left:467px;top:340px">04</span>
  <div class="step s4 right" style="left:205px;top:341px;width:253px">
    <h3>Is the physical product and packaging in a desirable condition?</h3>
    <p>Bottom-line: Nobody wants ripped or torn, or physically abused merchandise.</p>
  </div>

  <span class="num n5" style="left:705px;top:340px">05</span>
  <div class="step s5" style="left:759px;top:341px;width:290px">
    <h3>Is the item unique enough to where an alike SKU isn’t cannibalizing its sales?</h3>
    <p>Each SKU needs to be different and stand on its own. Eliminate redundancies in the product mix.</p>
  </div>

  <span class="num n6" style="left:795px;top:433px">06</span>
  <div class="step s6" style="left:850px;top:435px;width:300px">
    <h3>Do you have enough quantity of the item for the customer to want to make the purchase?</h3>
    <p>Seldom do consumers come in to buy one or two casters (i.e. project SKU). Having sufficient quantity to sell the job quantity is key</p>
  </div>

  <span class="num n7" style="left:826px;top:543px">07</span>
  <div class="step s7" style="left:877px;top:545px;width:290px">
    <h3>Is the item still relevant to the shopper?</h3>
    <p>Get rid of outdated product and technology… those old rotary dial phone cords!</p>
  </div>

  <span class="num n8" style="left:869px;top:640px">08</span>
  <div class="step s8" style="left:920px;top:638px;width:270px">
    <h3>Is the sale of the SKU independent of the sale of another item?</h3>
    <p>With SKUs that depend on each other to sell, analyze the sell through and performance of the other item.</p>
  </div>

  <section class="resources">
    <p>For further detail on in-stock position, see the following resources (click to visit link):</p>
    <nav class="links">
      <a href="#">Obsolete Inventory - Closeout Management (COM) Setup<sup>(URL)</sup></a>
      <span class="sep"></span>
      <a href="#">In-Stock Procedures<sup>(URL)</sup></a>
      <span class="sep"></span>
      <a href="#">Markdown Strategy<sup>(URL)</sup></a>
    </nav>
  </section>

  <div class="stripe-dark"></div>
  <div class="stripe-red"></div>
  <footer class="footer">
    <span>For more information, contact Store Systems and Operations:</span>
    <svg width="22" height="22" viewBox="0 0 22 22"><circle cx="11" cy="11" r="9.5" fill="none" stroke="#fff" stroke-width="1.4"/><path d="M7.6 6.2l1.8-.4 1 2.4-1.1.9a6 6 0 0 0 2.6 2.6l.9-1.1 2.4 1-.4 1.8c-3.9.4-7.6-3.3-7.2-7.2z" fill="#fff"/></svg>
    <span>555.014.2290</span>
    <span class="gap"></span>
    <svg width="22" height="16" viewBox="0 0 22 16"><rect x="1" y="1" width="20" height="14" fill="none" stroke="#fff" stroke-width="1.4"/><path d="M1 1l10 8 10-8" fill="none" stroke="#fff" stroke-width="1.4"/></svg>
    <span>storeoperations@birchlinesupply.example</span>
  </footer>
</main>
</body>
</html>
```